Business card design needed for Marbury Medical Practice

We need a new design for our growing medical practice. Our previous design used blue, white and black. I would like to have a design with a baby, child, adult and grandparent on it. We look after a wide range of patients from newborns to 100 year olds.

Industry/Entity Type

Medical

Contact Information for Business Card

Marbury Medical Practice
14 Dunmore Rd Kelmore, NSW 2791
Ph 4820 3647 Fax 4913 2506
Dr Helen Voss Dr Andrea Pollard
Dr Wendy Trelawny Dr Janice Whitworth
Dr Tom Ashbrook Dr Neil Dunn-Foster
Open Mon- Fri 9-1, 2-5pm
Sat 9-12pm by appointment
web:www.marburymedix.com.au
email:marburymedix@mailzonex.com

```html
<!DOCTYPE html>
<html lang="en">
<head>
<meta charset="utf-8">
<title>Marbury Medical Practice – Business Card</title>
<link rel="stylesheet" href="https://fonts.googleapis.com/css2?family=Tenor+Sans&display=swap">
<style>
  :root {
    --bg: #9ee8e6;
    --blue-deep: #2a76a3;
    --blue-light: #5aa9cf;
    --teal-band: #3c7f9b;
    --teal-band-dark: #336f89;
    --info-white: #f4f6f7;
    --info-grey: #dfe4e7;
    --ink: #1c1c1c;
    --address-blue: #2f7fa8;
    --white: #ffffff;
    --photo-light: #e9eaec;
    --photo-mid: #c9c5c2;
    --photo-warm: #b79a86;
  }
  * { box-sizing: border-box; margin: 0; padding: 0; }
  html, body { width: 1200px; height: 1000px; overflow: hidden; }
  body {
    background: var(--bg);
    font-family: "Tenor Sans", "Optima", sans-serif;
    position: relative;
  }
  .card {
    position: absolute;
    left: 220px;
    width: 760px;
    height: 440px;
    overflow: hidden;
    box-shadow: 0 10px 28px rgba(0, 60, 70, 0.28);
  }
  .card--front { top: 30px; }
  .card--back  { top: 510px; }

  /* Front */
  .front__header {
    position: absolute; inset: 0 0 auto 0; height: 200px;
    background: radial-gradient(ellipse at 55% 35%, var(--blue-light), var(--blue-deep) 75%);
  }
  .brand-mark {
    position: absolute; left: 50%; top: 28px; transform: translateX(-50%);
    width: 74px; height: 74px;
  }
  .brand-name {
    position: absolute; left: 0; right: 0; top: 122px;
    text-align: center; color: var(--white);
    font-size: 40px; letter-spacing: 0.5px; white-space: nowrap;
  }
  .front__info {
    position: absolute; left: 0; right: 0; top: 200px; height: 130px;
    background: linear-gradient(180deg, var(--info-white), var(--info-grey));
    display: flex; justify-content: space-between; padding: 18px 40px 0 56px;
  }
  .address { color: var(--ink); }
  .address__street {
    color: var(--address-blue); font-size: 19px; line-height: 24px;
    margin-bottom: 6px; white-space: nowrap;
  }
  .address__line { font-size: 13px; line-height: 19px; white-space: nowrap; }
  .doctors {
    display: grid; grid-template-columns: auto auto; column-gap: 26px; row-gap: 8px;
    list-style: none; font-size: 15px; line-height: 20px; color: var(--ink);
    padding-top: 8px; white-space: nowrap;
  }
  .doctors li::before { content: "•"; margin-right: 7px; }
  .front__footer {
    position: absolute; left: 0; right: 0; top: 330px; bottom: 0;
    background: var(--teal-band);
  }
  .front__footer::after {
    content: ""; position: absolute; left: 0; right: 0; top: 62px; height: 2px;
    background: var(--teal-band-dark);
  }
  .contact-web, .contact-email {
    position: absolute; top: 20px; color: var(--white); font-size: 15px; white-space: nowrap;
  }
  .contact-web { left: 80px; }
  .contact-email { right: 60px; }

  /* Back */
  .family-photo {
    position: absolute; inset: 0;
    background:
      radial-gradient(ellipse at 50% 70%, var(--photo-warm) 0%, var(--photo-mid) 40%, transparent 70%),
      linear-gradient(180deg, var(--photo-light), #d6d6d8);
  }
  .hours-band {
    position: absolute; left: 0; right: 0; top: 318px; height: 46px;
    background: var(--teal-band);
    color: var(--white); font-size: 18px; white-space: nowrap;
    display: flex; align-items: center; justify-content: center;
  }
</style>
</head>
<body>

<section class="card card--front" aria-label="Business card front">
  <div class="front__header">
    <svg class="brand-mark" viewBox="0 0 74 74" aria-hidden="true">
      <circle cx="37" cy="37" r="34" fill="none" stroke="#ffffff" stroke-width="2.5"/>
    </svg>
    <div class="brand-name">Marbury Medical Practice</div>
  </div>
  <div class="front__info">
    <div class="address">
      <p class="address__street">14 Dunmore Rd Kelmore</p>
      <p class="address__line">NSW 2791</p>
      <p class="address__line">Ph 4820 3647</p>
      <p class="address__line">Fax 4913 2506</p>
    </div>
    <ul class="doctors">
      <li>Dr Helen Voss</li>
      <li>Dr Andrea Pollard,</li>
      <li>Dr Wendy Trelawny</li>
      <li>Dr Janice Whitworth,</li>
      <li>Dr Tom Ashbrook</li>
      <li>Dr Neil Dunn-Foster</li>
    </ul>
  </div>
  <div class="front__footer">
    <span class="contact-web">web:www.marburymedix.com.au</span>
    <span class="contact-email">email:marburymedix@mailzonex.com</span>
  </div>
</section>

<section class="card card--back" aria-label="Business card back">
  <div class="family-photo" role="img" aria-label="Photograph of a smiling multi-generation family: young woman, young man holding a toddler, grandfather and grandmother, on a light grey studio background"></div>
  <div class="hours-band">Open Mon- Fri 9-1, 2-5pm Sat 9-12pm by appointment</div>
</section>

</body>
</html>
```